Flexx Yo

Need
Sexy image with girls dancing around my photo or background white and my photo cropped with the background out and then
Wurk
Dat
Body
Gurl

in red , I am looking for a huge Club feel
and I am open for new concepts but that should be a good start.

Target Market(s)

World Wide Appeal

Industry/Entity Type

Club

Requirements
Must have
• 1600 x 1600

Nice to have
• Women, concert crow club something unique royalty free images
Should not have
• nude or obscene photo's

```html
<!DOCTYPE html>
<html lang="en">
<head>
<meta charset="utf-8">
<title>Flexx Yo Body Gurl – Single Cover</title>
<link rel="stylesheet" href="https://fonts.googleapis.com/css2?family=Righteous&display=swap">
<style>
  :root {
    --ink-black: #050505;
    --stage-dark: #141414;
    --stage-mid: #4a4a4a;
    --stage-light: #b9b9b9;
    --title-white: #f4f4f4;
    --figure-top: #5a5a5a;
    --figure-bottom: #030303;
  }
  html, body {
    margin: 0;
    padding: 0;
    width: 1200px;
    height: 1200px;
    overflow: hidden;
    background: var(--ink-black);
  }
  .cover {
    position: relative;
    width: 1200px;
    height: 1200px;
    overflow: hidden;
    background:
      radial-gradient(ellipse 420px 620px at 690px 470px, var(--stage-light) 0%, var(--stage-mid) 45%, rgba(20,20,20,0) 100%),
      radial-gradient(ellipse 900px 700px at 640px 520px, var(--stage-mid) 0%, var(--stage-dark) 70%, var(--ink-black) 100%);
  }
  .light-rays {
    position: absolute;
    inset: 0;
  }
  .artist-photo {
    position: absolute;
    left: 0;
    top: 0;
  }
  .cover-title {
    position: absolute;
    left: 38px;
    top: 22px;
    margin: 0;
    font-family: "Righteous", sans-serif;
    font-weight: 400;
    font-size: 178px;
    line-height: 150px;
    letter-spacing: 6px;
    color: var(--title-white);
    text-transform: uppercase;
  }
  .cover-title span {
    display: block;
  }
</style>
</head>
<body>
  <main class="cover">
    <svg class="light-rays" width="1200" height="1200" viewBox="0 0 1200 1200" aria-hidden="true">
      <defs>
        <linearGradient id="ray" x1="0" y1="1" x2="0" y2="0">
          <stop offset="0" stop-color="#ffffff" stop-opacity="0.22"/>
          <stop offset="1" stop-color="#ffffff" stop-opacity="0"/>
        </linearGradient>
      </defs>
      <g fill="url(#ray)">
        <polygon points="690,620 520,0 600,0"/>
        <polygon points="690,620 760,0 860,0"/>
        <polygon points="690,620 960,0 1080,0"/>
        <polygon points="690,620 1200,140 1200,300"/>
        <polygon points="690,620 280,0 380,0"/>
        <polygon points="690,620 0,260 0,400"/>
        <polygon points="690,620 1200,520 1200,660"/>
      </g>
    </svg>

    <svg class="artist-photo" width="1200" height="1200" viewBox="0 0 1200 1200" role="img" aria-label="Photo of the artist in a dark suit, striped tie and sunglasses, cut out against the stage light">
      <defs>
        <linearGradient id="figure" x1="0" y1="0" x2="0" y2="1">
          <stop offset="0" stop-color="var(--figure-top)"/>
          <stop offset="0.35" stop-color="#1c1c1c"/>
          <stop offset="1" stop-color="var(--figure-bottom)"/>
        </linearGradient>
      </defs>
      <path d="M520 300 Q520 270 560 270 H720 Q760 270 760 300 V560 L940 640 Q1030 680 1040 760 V1200 H270 V760 Q280 680 370 640 L520 560 Z" fill="url(#figure)"/>
    </svg>

    <h1 class="cover-title">
      <span>Flexx</span>
      <span>Yo</span>
      <span>Body</span>
      <span>Gurl</span>
    </h1>
  </main>
</body>
</html>
```